Larkspur Ridge Management - Business Cards

I need business cards. My current logo was designed by a designer at this site and I very much like and am happy with the results. I would like a business card that is trendy, unique, current yet professional. I deal with high net worth clients daily

Target Market(s)

Out of state investors looking to get into the rental market in Ohio

Industry/Entity Type

Property Management, Consulting

Contact Information for Business Card

Name, Title (Chief Financial Officer) office phone number (555) 817-3094 website address larkridgemgmt.example

Font styles to use
Sans Serif

Colors
0054AA
0677BA
7BADD7
CADEEF
E8F1F8
0094D4
00A9DD
6FCCEA
C7EBF8
E9F6FB
00AB8E
00BBA5
67D7C9
C6EFE9
E9F9F6

```html
<!DOCTYPE html>
<html lang="en">
<head>
<meta charset="utf-8">
<title>Larkspur Ridge Management – Business Card</title>
<link rel="stylesheet" href="https://fonts.googleapis.com/css2?family=Fira+Sans:wght@400;600&display=swap">
<style>
  :root {
    --navy: #14266b;
    --navy-deep: #0f2460;
    --lavender: #8a90c6;
    --lavender-pale: #d4d6ef;
    --steel-blue: #2e4f8f;
    --ocean: #1d6597;
    --teal-blue: #2a86ad;
    --sky: #6fcCEA;
    --ink: #10275a;
    --white: #ffffff;
    --mist: #c9c9c9;
  }
  * { margin: 0; padding: 0; box-sizing: border-box; }
  html, body {
    width: 1200px;
    height: 686px;
    overflow: hidden;
  }
  body { background: var(--white); }
  .card {
    position: relative;
    width: 1200px;
    height: 686px;
    overflow: hidden;
    background:
      radial-gradient(ellipse 900px 420px at 380px 520px, #ffffff 0%, #fbfbfb 45%, rgba(255,255,255,0) 80%),
      linear-gradient(160deg, #bdbdbd 0%, #dedede 30%, #efefef 50%, #ffffff 70%);
    font-family: "Fira Sans", sans-serif;
  }
  .card__art {
    position: absolute;
    inset: 0;
    width: 1200px;
    height: 686px;
  }
  .identity {
    position: absolute;
    left: 114px;
    top: 292px;
    color: var(--ink);
  }
  .identity__name {
    font-weight: 600;
    font-size: 40px;
    line-height: 1;
    letter-spacing: 0.5px;
  }
  .identity__tagline {
    margin-top: 8px;
    font-weight: 400;
    font-size: 28.5px;
    line-height: 1.1;
    letter-spacing: 0.6px;
  }
  .brand {
    position: absolute;
    left: 958px;
    top: 137px;
    width: 140px;
    display: flex;
    flex-direction: column;
    align-items: center;
    gap: 12px;
  }
  .brand__square {
    width: 28px;
    height: 28px;
    background: var(--white);
  }
  .brand__name {
    color: var(--white);
    font-family: "Fira Sans", sans-serif;
    font-weight: 600;
    font-size: 19px;
    line-height: 1.2;
    text-align: center;
  }
</style>
</head>
<body>
  <main class="card">
    <svg class="card__art" viewBox="0 0 1200 686" aria-hidden="true">
      <defs>
        <linearGradient id="halo" x1="0" y1="0" x2="0.4" y2="1">
          <stop offset="0" stop-color="#6a70b0"/>
          <stop offset="1" stop-color="#e2e3f4"/>
        </linearGradient>
        <linearGradient id="navyFill" x1="0" y1="0" x2="0" y2="1">
          <stop offset="0" stop-color="#14266b"/>
          <stop offset="1" stop-color="#10245a"/>
        </linearGradient>
      </defs>
      <circle class="sweep sweep--steel" cx="1290" cy="760" r="460" fill="#2e4f8f"/>
      <circle class="sweep sweep--navy" cx="1330" cy="780" r="400" fill="#1a3478"/>
      <circle class="sweep sweep--ocean" cx="1400" cy="800" r="340" fill="#1d6597"/>
      <circle class="sweep sweep--teal" cx="1470" cy="830" r="280" fill="#2a7fa8"/>
      <circle class="sweep sweep--sky" cx="1540" cy="860" r="200" fill="#3b9cc4"/>
      <circle class="halo" cx="1118" cy="190" r="358" fill="url(#halo)" opacity="0.9"/>
      <circle class="disc" cx="1105" cy="184" r="324" fill="url(#navyFill)"/>
    </svg>

    <section class="identity">
      <h1 class="identity__name">LARK MGMT</h1>
      <p class="identity__tagline">Property Management &amp; Consulting</p>
    </section>

    <div class="brand">
      <span class="brand__square"></span>
      <span class="brand__name">Larkspur Ridge Management</span>
    </div>
  </main>
</body>
</html>
```